Afro-Fusion Music CD Cover

Nhambelo Collective is a Maputo, Mozambique-based band that combines rhythms and styles from across Africa. We are looking for a CD cover for the group’s first CD/ DVD release. We are looking for something dark, cool, funky, earthy and African – earth tones with a splash of deep and vibrant colour. All of our music was originally recorded across the continent as part of music for social change projects (gender, health awareness, etc) and combines Mozambican marrabenta, Senegalese mbalak, Nigerian afro beat, jazz, and much more. This band’s two singers, full horn section, throbbing bass, and rhythmic percussion creates an attention grabbing wall of fresh sounds, and lyrics are in English, French, Portuguese, Changaan, Sena, Swahili, and Zulu.

Visit website and listen to music….
http://www.nhambelocollective-band.test/
http://www.vidoramaplay.test/nhambelocollective

Reason: I have been on the road for work for the past 5 days and had problems getting online, so have been unable to provide feedback to designers, and so have extended 2 days to give time to offer feedback.

Target Market(s)

Lovers of African music, afro-beat, jazz – and music with a different edge

Industry/Entity Type

Health

Requirements
Must have
• • Able to give us in PSD or some sort of editable files so we can make small changes & add bar code.
• Back and front of the CD sleeves
• Conform to industry standard CD album art formats
• The groups logo is strong and should be prominently used.
• Reflect African influences, but not in a cheesy way.

Artist name: Nhambelo Collective
Album name: Night at Ponta Verde
Leave space for bar code.

Tracks:

1. Andiyiqondi
2. Bravos do Zambeze
3. Alertos Da Vida
4. Caminhos Cruzados
5. Cara Triste
6. Switha Hela
7. Nhambelo

8. Tavenor
9. Marrabenta minor
10 Protege tua vida
11. Kel's Jazz
12. Zamphan’ Izindlela
13. Crossroads
14. Pistes Croisees

Copyright: 2013 PRVL Productions
Recorded and Produced by Rupert Okonde

www.nhambelocollective-band.test
frendlypage.test/nhambelo.coletivo

```html
<!DOCTYPE html>
<html lang="en">
<head>
<meta charset="utf-8">
<title>Nhambelo Collective – Night at Ponta Verde</title>
<link rel="stylesheet" href="https://fonts.googleapis.com/css2?family=Fredoka:wght@600;700&display=swap">
<style>
  :root {
    --sky-top: #7a2f3a;
    --sky-glow: #f08a3a;
    --sky-light: #f6c98a;
    --horizon: #c8502a;
    --earth: #1a0707;
    --night: #0a0202;
    --band-red: #e0283c;
    --band-orange: #f06a2a;
    --band-cream: #f7e6da;
    --ink: #141010;
    --title-fill: #fbe9e4;
    --title-edge: #c4123a;
  }
  * { margin: 0; padding: 0; box-sizing: border-box; }
  html, body {
    width: 1200px; height: 1200px; overflow: hidden; background: var(--night);
  }
  .cover {
    position: relative; width: 1200px; height: 1200px; overflow: hidden;
    font-family: "Fredoka", sans-serif;
  }
  .landscape {
    position: absolute; inset: 0;
    background:
      radial-gradient(ellipse 55% 22% at 50% 40%, var(--sky-light) 0%, rgba(246,201,138,0) 70%),
      linear-gradient(180deg, var(--sky-top) 0%, #c9553e 14%, var(--sky-glow) 30%, var(--horizon) 42%, #3a0d0c 52%, var(--earth) 66%, var(--night) 100%);
  }
  .side-band {
    position: absolute; top: 0; bottom: 0; width: 72px;
  }
  .side-band--left {
    left: 0;
    background: linear-gradient(90deg, var(--band-cream) 0 14px, var(--band-red) 14px 30px, var(--night) 30px 38px, var(--band-orange) 38px 56px, rgba(0,0,0,0) 56px);
  }
  .side-band--right {
    right: 0;
    background: linear-gradient(270deg, var(--band-cream) 0 14px, var(--band-red) 14px 30px, var(--night) 30px 38px, var(--band-orange) 38px 56px, rgba(0,0,0,0) 56px);
  }
  .band-name {
    position: absolute; left: 0; right: 0; top: 190px;
    display: flex; align-items: center; justify-content: center; gap: 36px;
  }
  .band-name__mark {
    flex: none; width: 150px; height: 150px; border-radius: 50%; background: var(--ink);
  }
  .band-name__text {
    font-weight: 700; font-size: 112px; line-height: 1.02; color: var(--ink);
    letter-spacing: 2px;
  }
  .band-name__line { display: block; }
  .album-title {
    position: absolute; left: 258px; top: 842px;
    color: var(--title-fill); font-weight: 700; line-height: 1;
    -webkit-text-stroke: 3px var(--title-edge);
    paint-order: stroke fill;
    text-shadow: 0 0 6px rgba(0,0,0,0.7);
  }
  .album-title__line { display: block; font-size: 66px; white-space: nowrap; }
  .album-title__line--second { margin-left: 138px; margin-top: 18px; }
  .album-title__initial { font-size: 104px; }
  .album-title__small { font-size: 48px; margin-left: 40px; }
</style>
</head>
<body>
  <main class="cover">
    <div class="landscape" role="img" aria-label="Sunset sky in red and orange over silhouetted acacia trees and dark savanna grass"></div>
    <div class="side-band side-band--left" role="img" aria-label="Vertical zigzag border in red, orange and cream"></div>
    <div class="side-band side-band--right" role="img" aria-label="Vertical zigzag border in red, orange and cream"></div>

    <div class="band-name">
      <span class="band-name__mark"></span>
      <span class="band-name__text">
        <span class="band-name__line">Nhambelo</span>
        <span class="band-name__line">Collective</span>
      </span>
    </div>

    <h1 class="album-title">
      <span class="album-title__line"><span class="album-title__initial">N</span>ight<span class="album-title__small">AT</span></span>
      <span class="album-title__line album-title__line--second"><span class="album-title__initial">P</span>onta Verde</span>
    </h1>
  </main>
</body>
</html>
```